Landing Page für Kornwiese-Prüfset.de
Zielgruppe
Domain: Kornwiese-Prüfset.de
THC Schnelltests mit gringer Anzeigegrenze mit 5ng/ml, ausgerichtet auf die Selbstkontrolle für die Fahrtauglichkeit (Grenze im Gesetz 3,5ng/ml)
Farbe: grün
Anregung siehe Bild
Aufgabenstellung
- Conversionoptimiert
- Soll auf unseren Webshop www.rv-vitalis.de verlinken

```html
<!DOCTYPE html>
<html lang="de">
<head>
<meta charset="utf-8">
<title>Kornwiese-Prüfset.de – Mach den Selbsttest</title>
<link href="https://fonts.googleapis.com/css2?family=Rubik:ital,wght@0,400;0,500;0,700;1,400;1,700;1,800;1,900&family=Lato:ital,wght@0,700;1,400&display=swap" rel="stylesheet">
<style>
  :root{
    --green-dark:#27591f;
    --green:#2f6b28;
    --green-mid:#3d7a33;
    --green-light:#6a9a5e;
    --cream:#fff5d6;
    --orange:#f0a01a;
    --grey-bg:#f2f2f2;
    --footer:#3d3d3d;
    --text:#2a4d22;
  }
  *{box-sizing:border-box;margin:0;padding:0}
  html,body{width:1200px;height:2843px;overflow:hidden;background:#fff}
  body{position:relative;font-family:"Rubik",sans-serif;color:var(--text)}
  .abs{position:absolute}

  /* Hero */
  .hero{left:0;top:0;width:1200px;height:537px;overflow:hidden;
    background:radial-gradient(ellipse at 55% 25%,#3f7d35 0%,#2d6226 45%,#234f1d 100%)}
  .hero-plant{left:830px;top:150px;width:330px;height:390px;border-radius:45% 45% 20% 20%;
    background:radial-gradient(ellipse at 50% 45%,#4ea842 0%,#2f7e3a 50%,rgba(35,79,29,0) 75%)}
  .hero-band{left:0;top:0}
  .brand{display:flex;align-items:center;gap:10px;font-weight:700;letter-spacing:.5px}
  .hero .brand{left:87px;top:58px;font-size:36px;color:var(--cream)}
  .hero .brand .mark{background:var(--cream);width:34px;height:34px}
  .hero-title{left:145px;top:182px;font-weight:900;font-style:italic;font-size:70px;line-height:76px;color:var(--cream);text-transform:uppercase}
  .hero-sub{left:145px;top:340px;font-style:italic;font-size:30px;color:var(--cream);text-transform:uppercase}
  .bubble{left:684px;top:142px;width:180px;height:148px}
  .bubble-text{left:720px;top:176px;width:130px;font-weight:800;font-style:italic;font-size:14px;line-height:16.5px;color:var(--green-dark);text-transform:uppercase}

  /* Partner strip */
  .partners{left:87px;top:560px;width:1025px;height:68px;display:flex;justify-content:space-between;align-items:center}
  .partner{height:40px;border-radius:6px;background:#e6e6e6}

  /* Content blocks */
  .photo{overflow:hidden}
  .photo-people{left:87px;top:656px;width:508px;height:467px;
    background:linear-gradient(180deg,#2e6a27 0%,#2b5f24 55%,#235019 100%)}
  .photo-test{left:605px;top:1163px;width:508px;height:466px;
    background:linear-gradient(135deg,#2f6a28 0%,#3b7b33 50%,#6d9a68 78%,#2f6a28 100%)}
  .photo-caption{font-weight:900;font-style:italic;font-size:36px;line-height:44px;color:var(--cream);text-transform:uppercase}
  .photo-caption small{display:block;font-weight:400;font-size:21px;line-height:28px}
  .photo-people .photo-caption{left:37px;top:310px}
  .photo-test .photo-caption{left:37px;top:310px}

  .text-col{display:flex;flex-direction:column;align-items:flex-start}
  .section-head{font-weight:800;font-style:italic;font-size:22px;line-height:27px;color:var(--green-dark);text-transform:uppercase}
  .rule{width:68px;height:7px;background:var(--green-dark);flex:none}
  .copy{font-size:13px;line-height:19px;color:var(--text)}
  .copy p{margin-bottom:18px}
  .copy p:last-child{margin-bottom:0}

  .cta{left:87px;top:1686px;width:1025px;height:65px;border-radius:33px;background:var(--orange);
    color:#fff;font-weight:800;font-style:italic;font-size:18px;display:flex;align-items:center;justify-content:center;text-decoration:none;text-transform:uppercase}

  .testimonial{left:0;top:1808px;width:1200px;height:246px;background:var(--grey-bg)}
  .quote{left:258px;top:100px;width:684px;text-align:center;font-family:"Lato",sans-serif;font-style:italic;font-size:16.5px;line-height:22px;color:#555}
  .quote-author{left:0;top:184px;width:1200px;text-align:center;font-family:"Lato",sans-serif;font-weight:700;font-size:17px;color:#444}
  .qmark{font-family:"Lato",sans-serif;font-weight:700;font-size:110px;line-height:1;color:#c8c8c8}

  /* Contact */
  .field{background:var(--cream);font-size:13px;color:#555;padding:0 18px;display:flex;align-items:center}
  .field.area{align-items:flex-start;padding-top:16px}
  .consent{left:87px;top:2632px;font-size:15px;color:#444;display:flex;align-items:center;gap:8px}
  .consent .box{width:18px;height:18px;background:var(--cream)}
  .consent a{color:var(--orange);text-decoration:none}
  .submit{left:87px;top:2692px;width:259px;height:65px;border-radius:33px;background:var(--green-dark);color:#fff;
    font-weight:800;font-style:italic;font-size:18px;display:flex;align-items:center;justify-content:center;text-transform:uppercase}
  .divider{left:724px;top:2261px;width:1px;height:386px;background:#e2e2e2}
  .contact-brand{left:767px;top:2274px;font-size:38px;color:var(--green-dark)}
  .contact-brand .mark{background:var(--green-dark);width:38px;height:38px}
  .info{left:767px;display:flex;align-items:center;gap:14px;font-size:13px;line-height:18px;color:#333}
  .info .icon{width:51px;height:51px;border-radius:50%;background:var(--green-dark);display:flex;align-items:center;justify-content:center}
  .info b{display:block;font-weight:700}

  .footer{left:0;top:2793px;width:1200px;height:50px;background:var(--footer);color:#fff;font-size:13px;display:flex;align-items:center;padding:0 87px}
  .footer nav{display:flex;gap:22px;margin-left:36px}
  .footer .social{margin-left:auto;display:flex;gap:14px}
  .footer .social span{width:20px;height:20px;border-radius:50%;background:#fff}
</style>
</head>
<body>

<header class="abs hero" role="img" aria-label="Foto einer jungen Frau am Steuer eines Autos in grüner Einfärbung, rechts eine Cannabispflanze">
  <div class="abs hero-plant"></div>
  <svg class="abs hero-band" width="1200" height="537" viewBox="0 0 1200 537">
    <polygon points="0,537 820,424 1200,420 1200,537" fill="var(--green-light)"/>
  </svg>
  <div class="abs brand"><span class="mark"></span>RV-Vitalis</div>
  <h1 class="abs hero-title">Mach den<br>Selbsttest.</h1>
  <p class="abs hero-sub">Gefährde nicht deinen Führerschein!</p>
  <svg class="abs bubble" viewBox="0 0 180 148">
    <path d="M14 68 C10 22 60 0 110 4 C155 8 184 40 174 78 C164 118 122 134 78 132 C44 130 18 110 14 68 Z" fill="var(--cream)"/>
  </svg>
  <p class="abs bubble-text">Im Straßen-<br>verkehr liegt<br>die Grenze bei<br>3,5ng/ml.</p>
</header>

<div class="abs partners" aria-label="Partner">
  <span class="partner" style="width:122px"></span>
  <span class="partner" style="width:170px"></span>
  <span class="partner" style="width:145px"></span>
  <span class="partner" style="width:58px"></span>
  <span class="partner" style="width:112px"></span>
</div>

<section>
  <div class="abs photo photo-people" role="img" aria-label="Gruppenfoto lachender Menschen in grüner Einfärbung">
    <p class="abs photo-caption">Gemeinsam<br>für mehr Sicherheit.<small>Für euch und eurer Zukunft.</small></p>
  </div>
  <div class="abs text-col" style="left:644px;top:716px;width:470px">
    <h2 class="section-head">Wir sind für euch da.</h2>
    <div class="rule" style="margin:10px 0 31px 1px"></div>
    <div class="copy">
      <p>Ihr benötigt qualitativ hochwertige Produkte? RV-Vitalis ist für Sie da. Wir bieten geprüfte Hilfsmittel für Heimanwender, Testzentren, Ärzte, Krankenhäuser und Gewerbetreibende, mit denen Sie sicher durch den Alltag kommen.</p>
      <p>Durch die Gesetzesänderung in Bezug auf Cannabis werden Drogenschnelltests in Zukunft in bestimmten Situationen unverzichtbar sein. Bestellen Sie bei uns hochwertige Schnelltests auf z.B. THC oder Amphetamine zu attraktiven Preisen.</p>
      <p>Unser Fachpersonal unterstützt Sie gerne bei Fragen zu unserem Sortiment. Mit 11 Jahren Erfahrung unterstützen wir Sie gerne bei der umfassenden Pandemie- und Gesundheitsvorsorge.</p>
      <p>Moderne Produkte und hohe Fertigungsstandards gepaart mit qualifiziertem</p>
    </div>
  </div>
</section>

<section>
  <div class="abs text-col" style="left:107px;top:1226px;width:480px">
    <h2 class="section-head" style="font-size:21px;letter-spacing:-.2px;white-space:nowrap">THC Drogenschnelltest 5ng (Cannabis,<br>Marihuana, Haschisch), 5 ng/m</h2>
    <div class="rule" style="margin:13px 0 32px"></div>
    <div class="copy" style="line-height:20px;width:475px">
      <p>Ein THC-Urintest ist ein diagnostisches Verfahren, mit dem Tetrahydrocannabinol (THC), der psychoaktive Wirkstoff von Cannabis, im Urin nachgewiesen werden kann. Der Test beruht auf der Tatsache, dass THC und seine Metaboliten nach dem Konsum von Cannabis noch einige Zeit im Körper verbleiben und über den Urin ausgeschieden werden können.</p>
      <p>Der Test wird häufig eingesetzt, um den Konsum von Cannabis nachzuweisen, insbesondere bei Drogentests, am Arbeitsplatz oder in Gerichtsverfahren.</p>
      <p>Es ist wichtig zu beachten, dass ein positiver THC-Urintest nicht unbedingt bedeutet, dass die Person zum Zeitpunkt des Tests unter dem Einfluss von Cannabis steht, sondern lediglich, dass sie in der Vergangenheit Cannabis konsumiert hat.</p>
    </div>
  </div>
  <div class="abs photo photo-test" role="img" aria-label="Frau mit einer THC-Testkassette in grüner Einfärbung">
    <p class="abs photo-caption">Einfach und<br>unkompliziert<small>Testergebnis nach 5 Minuten</small></p>
  </div>
</section>

<a class="abs cta" href="https://www.rv-vitalis.de">Hier geht es zum Shop</a>

<section class="abs testimonial">
  <span class="abs qmark" style="left:962px;top:34px">”</span>
  <span class="abs qmark" style="left:185px;top:146px">”</span>
  <p class="abs quote">Lorem ipsum dolor sit amet, consetetur sadipscing elitr, sed diam nonumy eirmod tempor invidunt ut labore et dolore magna aliquyam erat, sed diam voluptua. At vero eos et accusam et justo duo dolores et ea rebum.</p>
  <p class="abs quote-author">KM aus Potsdam</p>
</section>

<section>
  <div class="abs text-col" style="left:87px;top:2140px">
    <h2 class="section-head">Hast du Fragen?<br>Dann nimm doch Kontakt mit uns auf.</h2>
    <div class="rule" style="margin-top:15px"></div>
  </div>

  <div class="abs field" style="left:87px;top:2274px;width:288px;height:40px">Name</div>
  <div class="abs field" style="left:386px;top:2274px;width:296px;height:40px">E-Mailadresse</div>
  <div class="abs field" style="left:87px;top:2328px;width:595px;height:40px">Betreff</div>
  <div class="abs field area" style="left:87px;top:2382px;width:595px;height:229px">Ihre Nachricht</div>
  <label class="abs consent"><span class="box"></span>Ich akzeptiere die <a href="#">Datenschutzbestimmungen</a> und die Verarbeitung meiner Daten.</label>
  <div class="abs submit">Anfrage senden</div>

  <div class="abs divider"></div>
  <div class="abs brand contact-brand"><span class="mark"></span>RV-Vitalis</div>

  <div class="abs info" style="top:2366px">
    <span class="icon"><svg width="22" height="22" viewBox="0 0 24 24" fill="none" stroke="#fff" stroke-width="1.8"><path d="M12 22s7-7 7-12a7 7 0 0 0-14 0c0 5 7 12 7 12z"/><circle cx="12" cy="10" r="2.5"/></svg></span>
    <div><b>Adresse:</b>Lindenweg 12 , 18435 Stralsund</div>
  </div>
  <div class="abs info" style="top:2442px">
    <span class="icon"><svg width="22" height="22" viewBox="0 0 24 24" fill="none" stroke="#fff" stroke-width="1.8"><rect x="3" y="5" width="18" height="14" rx="2"/><path d="M3 7l9 6 9-6"/></svg></span>
    <div><b>E-Mail:</b>info[at]rv-vitalis.de</div>
  </div>
  <div class="abs info" style="top:2516px">
    <span class="icon"><svg width="22" height="22" viewBox="0 0 24 24" fill="none" stroke="#fff" stroke-width="1.8"><path d="M5 3h4l2 5-3 2a11 11 0 0 0 6 6l2-3 5 2v4a2 2 0 0 1-2 2A17 17 0 0 1 3 5a2 2 0 0 1 2-2z"/></svg></span>
    <div><b>Telefon:</b>+49 &nbsp;(0)800 12 34 567</div>
  </div>
  <div class="abs info" style="top:2590px">
    <span class="icon"><svg width="22" height="22" viewBox="0 0 24 24" fill="none" stroke="#fff" stroke-width="1.8"><path d="M12 22s7-7 7-12a7 7 0 0 0-14 0c0 5 7 12 7 12z"/><circle cx="12" cy="10" r="2.5"/></svg></span>
    <div><b>Web:</b>www.rv-vitalis.de</div>
  </div>
</section>

<footer class="abs footer">
  <span>© 2024 Medizin- und Praxisbedarf online kaufen - RV-Vitalis - Alle Rechte vorbehalten.</span>
  <nav><span>Impressum</span><span>Datenschutz</span><span>Cookie-Richtlinie (EU)</span></nav>
  <div class="social"><span></span><span></span></div>
</footer>

</body>
</html>
```